10 years employment working at VALMIR

I need a certificate designed for employees to recognise 10 year tenure at our company. 1. You need to feature our logo 2. Our Grounds design. 3. Our Purpose: To provide support and service that enables disadvantaged and/or unemployed people in our community to secure and sustain meaningful employment. 4. A space for the employees name 5. A space for our Lara Bexley CEO and Grover Lunt, Chair of Board to sign 6. VALMIR Values your Service and Contribution

Target Market(s)

Employees

Industry/Entity Type

Employment Agency

Font styles to use
Sans Serif

Requirements
Must have
• Every thing from number 1 to 6 above in the description

```html
<!DOCTYPE html>
<html lang="en">
<head>
<meta charset="UTF-8">
<title>VALMIR – Certificate of Appreciation</title>
<link rel="stylesheet" href="https://fonts.googleapis.com/css2?family=Montserrat:wght@700;800&family=Playball&family=Lora:ital,wght@0,400;1,600;1,700&display=swap">
<style>
  :root {
    --teal: #1f9c7e;
    --teal-deep: #1a6e66;
    --slate: #2f4d53;
    --lime: #7dc142;
    --orange: #f7a93b;
    --ink: #2e2e35;
    --grey-text: #555;
    --paper: #ffffff;
    --seal: #eeeff1;
  }
  * { margin: 0; padding: 0; box-sizing: border-box; }
  html, body { width: 1200px; height: 848px; overflow: hidden; background: #000; }
  .certificate {
    position: relative;
    width: 1200px;
    height: 848px;
    overflow: hidden;
  }
  .grounds-pattern {
    position: absolute;
    inset: 0;
    background:
      radial-gradient(ellipse 160px 260px at 70px 424px, var(--teal) 0%, transparent 100%),
      radial-gradient(ellipse 160px 260px at 1130px 424px, var(--teal) 0%, transparent 100%),
      radial-gradient(ellipse 220px 180px at 200px 110px, rgba(247,169,59,.55) 0%, transparent 100%),
      radial-gradient(ellipse 220px 180px at 1000px 110px, rgba(247,169,59,.55) 0%, transparent 100%),
      radial-gradient(ellipse 220px 180px at 200px 740px, rgba(247,169,59,.55) 0%, transparent 100%),
      radial-gradient(ellipse 220px 180px at 1000px 740px, rgba(247,169,59,.55) 0%, transparent 100%),
      linear-gradient(90deg, var(--teal-deep), var(--slate) 30%, var(--teal) 50%, var(--slate) 70%, var(--teal-deep));
  }
  .panel {
    position: absolute;
    left: 144px;
    top: 107px;
    width: 912px;
    height: 635px;
    background: var(--paper);
    border: 5px solid var(--orange);
  }
  .panel::after {
    content: "";
    position: absolute;
    inset: 5px;
    border: 1.5px solid var(--orange);
  }
  .panel-content {
    position: absolute;
    inset: 0;
    text-align: center;
  }
  .rule-ornament {
    position: absolute;
    left: 0;
    width: 100%;
  }
  .rule-ornament--top { top: 70px; }
  .rule-ornament--bottom { top: 207px; }
  .title {
    position: absolute;
    top: 89px;
    left: 0;
    width: 100%;
    font-family: "Montserrat", sans-serif;
    font-weight: 800;
    font-size: 65px;
    line-height: 1;
    letter-spacing: 1px;
    color: var(--lime);
  }
  .subtitle {
    position: absolute;
    top: 155px;
    left: 0;
    width: 100%;
    font-family: "Playball", cursive;
    font-size: 46px;
    line-height: 1;
    color: var(--ink);
  }
  .recipient-name {
    position: absolute;
    top: 277px;
    left: 0;
    width: 100%;
    font-family: "Lora", serif;
    font-style: italic;
    font-weight: 700;
    font-size: 30px;
    line-height: 1;
    color: var(--ink);
  }
  .recipient-line {
    position: absolute;
    top: 313px;
    left: 278px;
    width: 356px;
    height: 1.5px;
    background: var(--lime);
  }
  .tagline {
    position: absolute;
    top: 327px;
    left: 0;
    width: 100%;
    font-family: "Lora", serif;
    font-style: italic;
    font-weight: 700;
    font-size: 13px;
    letter-spacing: .5px;
    color: var(--ink);
  }
  .purpose {
    position: absolute;
    top: 357px;
    left: 0;
    width: 100%;
    font-family: "Lora", serif;
    font-size: 14.5px;
    line-height: 19px;
    color: var(--ink);
  }
  .seal {
    position: absolute;
    left: 370px;
    top: 432px;
    width: 172px;
    height: 172px;
  }
  .seal-name {
    position: absolute;
    left: 0;
    top: 66px;
    width: 100%;
    font-family: "Montserrat", sans-serif;
    font-weight: 800;
    font-size: 30px;
    line-height: 1.2;
    letter-spacing: -.5px;
    color: #111;
    text-align: center;
  }
  .signatory {
    position: absolute;
    top: 516px;
    width: 155px;
    text-align: center;
    font-family: "Lora", serif;
    color: var(--grey-text);
  }
  .signatory--ceo { left: 160px; }
  .signatory--chair { left: 599px; }
  .signatory-line {
    height: 1.5px;
    background: var(--lime);
    margin-bottom: 4px;
  }
  .signatory-name {
    font-style: italic;
    font-weight: 700;
    font-size: 13px;
    line-height: 16px;
  }
  .signatory-role {
    font-size: 14px;
    line-height: 16px;
  }
</style>
</head>
<body>
<main class="certificate">
  <div class="grounds-pattern" role="img" aria-label="VALMIR grounds pattern: flowing teal and green patterned bands with golden leaf motifs"></div>

  <section class="panel">
    <div class="panel-content">
      <svg class="rule-ornament rule-ornament--top" width="912" height="14" viewBox="0 0 912 14" aria-hidden="true">
        <line x1="296" y1="7" x2="420" y2="7" stroke="#7dc142" stroke-width="3"/>
        <circle cx="456" cy="7" r="5" fill="none" stroke="#7dc142" stroke-width="2.5"/>
        <line x1="492" y1="7" x2="616" y2="7" stroke="#7dc142" stroke-width="3"/>
      </svg>

      <h1 class="title">CERTIFICATE</h1>
      <p class="subtitle">of appreciation</p>

      <svg class="rule-ornament rule-ornament--bottom" width="912" height="14" viewBox="0 0 912 14" aria-hidden="true">
        <line x1="410" y1="7" x2="444" y2="7" stroke="#7dc142" stroke-width="2.5"/>
        <circle cx="456" cy="7" r="5" fill="none" stroke="#7dc142" stroke-width="2.5"/>
        <line x1="468" y1="7" x2="502" y2="7" stroke="#7dc142" stroke-width="2.5"/>
      </svg>

      <p class="recipient-name">Name Come Here</p>
      <div class="recipient-line"></div>
      <p class="tagline">VALMIR Values your Service and Contribution</p>
      <p class="purpose">
        Our Purpose: To provide support and service that enables<br>
        disadvantaged and/or unemployed people in our community<br>
        to secure and sustain meaningful employment.
      </p>

      <div class="signatory signatory--ceo">
        <div class="signatory-line"></div>
        <p class="signatory-name">Lara Bexley</p>
        <p class="signatory-role">CEO</p>
      </div>

      <div class="seal">
        <svg width="172" height="172" viewBox="0 0 172 172" aria-hidden="true">
          <circle cx="88" cy="90" r="80" fill="#dcdde0"/>
          <circle cx="86" cy="86" r="80" fill="#eeeff1"/>
        </svg>
        <p class="seal-name">VALMIR</p>
      </div>

      <div class="signatory signatory--chair">
        <div class="signatory-line"></div>
        <p class="signatory-name">Grover Lunt</p>
        <p class="signatory-role">CHAIR OF BOARD</p>
      </div>
    </div>
  </section>
</main>
</body>
</html>
```